Educational Institution needs a new website

A little bit about ourselves:
Bramwell College is a multicultural K-12 school with students who represent nearly 30 ethnic and cultural backgrounds. It is one of the fastest growing schools in the City of Torvale (in Perth, Western Australia), and offers quality education with a unique school environment at two campuses.
The mission of Bramwell College is to equip students with moral values, academic knowledge and 21st century skills. We empower students to unlock their potential to be confident global citizens.
Bramwell College strives to educate students in a manner which inspires them to become lifelong learners. We are committed to raising individuals who are tolerant and respectful towards others enabling them to grow into citizens who contribute to the common good of society.
Here are our design goals:
#1: To emphasise the growth of the school from a small school community to a much larger prestigious college.
#2: Have current and prospective parents have a clear understanding of our college’s morals and values and how we differ from other colleges.
#3: Highlight that our school provides a joyful and safe environment, which is highly valued by parents.
#4: Emphasise that our school presents a welcoming atmosphere for parents as we have strong relationships with our community.
#5: Highlight the various after-school activities available to our students, which are provided through the clubs and pastoral care department.
#6: Allow for online registrations and the option of adding student, staff and parent portals.
#7: Follow the existing school colours
We would like to request the design for the home page and a secondary page to see the alternative layouts.
Other information:
Please note that our logo is will be changed slightly in the upcoming weeks. Please keep this in mind while designing.
We will have another contest for the coding of the website.
We want to be able to make amendments and additions to the content of the website in the future and would like to make sure we have a strong communication with the designer.
The existing website is https://www.bramwellcol.example.edu.au/ for reference for school colours and content.
Industry/Entity Type
Education
Number of Pages Required
1 page

```html
<!DOCTYPE html>
<html lang="en">
<head>
<meta charset="utf-8">
<title>Bramwell College</title>
<link href="https://fonts.googleapis.com/css2?family=Montserrat:wght@400;500;600;700&display=swap" rel="stylesheet">
<style>
:root{
  --navy:#083a66;
  --blue:#1a66a3;
  --mid:#2f7fc1;
  --sky:#2a9fdb;
  --grey:#f3f3f3;
  --ink:#1c1c1c;
  --text:#333;
  --white:#fff;
}
*{margin:0;padding:0;box-sizing:border-box}
html,body{width:1200px;height:3012px;overflow:hidden}
body{position:relative;font-family:'Montserrat',sans-serif;color:var(--text);background:var(--white)}
.abs{position:absolute}
/* header */
.brand{left:88px;top:18px;display:flex;flex-direction:column;align-items:center;gap:8px}
.brand-dot{width:52px;height:52px;border-radius:50%;background:var(--sky)}
.brand-name{font-size:19px;font-weight:700;color:var(--blue);letter-spacing:.5px}
.social{display:flex;gap:8px}
.social span{width:28px;height:28px;border-radius:50%;background:var(--blue);display:block}
.social span.on{background:var(--sky)}
.top-social{left:790px;top:26px}
.search{left:906px;top:25px;width:205px;height:32px;border:1px solid #ccc;border-radius:16px;font-size:14px;color:#666;padding:7px 16px}
.search i{position:absolute;right:2px;top:2px;width:26px;height:26px;border-radius:50%;background:var(--blue)}
.nav{left:372px;top:79px;width:739px;display:flex;justify-content:space-between;font-size:14.5px;color:var(--ink)}
/* hero */
.hero{left:0;top:117px}
.portal{left:129px;top:485px;width:259px;height:582px;border-radius:130px;background:var(--blue);color:var(--white);text-align:center}
.portal-item{position:absolute;left:0;width:100%;display:flex;flex-direction:column;align-items:center}
.portal-item b{font-size:21px;font-weight:600;letter-spacing:.5px;line-height:1.1}
.portal-item small{font-size:15px;line-height:1.1}
.staff-ring{position:absolute;left:58px;top:220px;width:144px;height:144px;border-radius:50%;background:var(--sky)}
/* about */
.about{left:483px;top:748px;width:610px}
.about h2{font-size:35px;font-weight:500;color:var(--blue);letter-spacing:.5px}
.about h3{margin-top:14px;font-size:17px;font-weight:600;color:var(--ink);line-height:24px;width:460px}
.about p{margin-top:26px;font-size:13.4px;line-height:20px;color:#444}
.btn{display:inline-block;margin-top:28px;width:135px;height:32px;border-radius:6px;background:var(--blue);color:var(--white);font-size:14px;text-align:center;line-height:32px}
/* campuses */
.grey{left:0;top:1150px;width:1200px;height:520px;background:var(--grey)}
.photo{display:block}
.campus-box{width:180px;height:146px;background:var(--blue);border-radius:6px;color:var(--white);text-align:center;padding-top:28px}
.campus-box h4{font-size:18px;font-weight:600;line-height:24px;letter-spacing:.5px}
.pill{display:inline-block;margin-top:16px;padding:0 14px;height:32px;line-height:32px;border-radius:5px;background:var(--sky);font-size:14px}
.pill-alt{background:var(--mid)}
/* announcements */
.navy{left:0;top:1765px;width:1200px;height:470px;background:var(--navy)}
.ann-title{left:0;top:1780px;width:1200px;text-align:center;font-size:35px;font-weight:600;color:var(--white);letter-spacing:.5px}
.card-box{width:282px;height:111px;background:var(--white);padding:20px 24px 0}
.card-box h5{font-size:16px;font-weight:500;color:var(--blue);line-height:20px}
.meta{margin-top:18px;display:flex;gap:18px;font-size:11.5px;color:#333;align-items:center}
.meta span{display:flex;align-items:center;gap:5px}
.drag{left:1079px;top:1967px;width:64px;height:64px;border-radius:50%;background:var(--white);text-align:center;font-size:10px;color:#222;padding-top:14px;box-shadow:0 2px 6px rgba(0,0,0,.2)}
/* quick links */
.quick{width:170px;height:170px;border-radius:50%;background:var(--white);box-shadow:0 0 0 3px #eee,0 2px 10px rgba(0,0,0,.08);display:flex;flex-direction:column;align-items:center;justify-content:center;text-align:center;font-size:14px;font-weight:500;color:var(--ink);line-height:18px;gap:10px}
.quick.active{background:var(--sky);color:var(--white);box-shadow:0 0 0 3px #e6f3fb}
/* footer */
.foot{left:0;top:2835px;width:1200px;height:140px;background:var(--navy)}
.ribbon{left:88px;top:2848px;width:400px;color:var(--white)}
.ribbon h6{font-size:16px;font-weight:700;letter-spacing:.3px}
.ribbon p{margin-top:14px;font-size:12.3px;line-height:18px}
.ribbon u{text-decoration:underline}
.stat{color:var(--white);text-align:center}
.stat small{font-size:12px;display:block}
.stat b{font-size:16px;font-weight:700;display:block;margin-top:8px;letter-spacing:.5px}
.divider{left:951px;top:2890px;width:1px;height:52px;background:rgba(255,255,255,.4)}
.bar{left:0;top:2975px;width:1200px;height:37px;background:var(--sky);color:var(--white);font-size:12.5px;padding:11px 88px}
.bottom-social{left:1012px;top:2980px}
.bottom-social span{background:var(--blue)}
</style>
</head>
<body>

<header>
  <div class="abs brand"><span class="brand-dot"></span><span class="brand-name">Bramwell College</span></div>
  <div class="abs social top-social" aria-label="Social links"><span></span><span></span><span class="on"></span></div>
  <div class="abs search">Search<i></i></div>
  <nav class="abs nav"><span>About Us</span><span>Learning</span><span>Student Life</span><span>Enrolment</span><span>Community</span><span>News &amp; Events</span><span>Contact Us</span></nav>
</header>

<svg class="abs hero" width="1200" height="620" viewBox="0 0 1200 620">
  <defs><linearGradient id="heroGrad" x1="0" y1="0" x2="1" y2="1"><stop offset="0" stop-color="#c9a890"/><stop offset=".5" stop-color="#8a6c5c"/><stop offset="1" stop-color="#c98e96"/></linearGradient></defs>
  <path role="img" aria-label="Young students playing with coloured building blocks in a classroom" fill="url(#heroGrad)" d="M0 0H1200V400C1100 555 900 585 780 565C600 535 400 465 250 465C130 465 50 495 0 515Z"/>
  <path fill="#2c79bd" d="M0 515C50 495 130 465 250 465C400 465 600 535 780 565C900 585 1100 555 1200 400V455C1100 615 900 625 770 600C600 575 420 515 260 515C130 515 50 560 0 595Z"/>
  <g fill="none" stroke="#2a9fdb" stroke-width="2"><circle cx="571" cy="423" r="7"/><circle cx="599" cy="423" r="7"/><circle cx="628" cy="423" r="7"/></g>
  <circle cx="599" cy="423" r="3" fill="#2a9fdb"/>
</svg>

<section class="abs portal">
  <div class="portal-item" style="top:72px">
    <svg width="52" height="50" viewBox="0 0 52 50" fill="none" stroke="#fff" stroke-width="2.2"><path d="M4 14L26 4L48 14L26 24Z"/><path d="M12 18V30C12 38 40 38 40 30V18"/><path d="M48 14V28"/></svg>
    <b style="margin-top:12px">STUDENT</b><small>Portal</small>
  </div>
  <div class="staff-ring"></div>
  <div class="portal-item" style="top:246px">
    <svg width="44" height="48" viewBox="0 0 44 48" fill="none" stroke="#fff" stroke-width="2.2"><circle cx="22" cy="12" r="9"/><path d="M4 46C4 30 12 26 22 26C32 26 40 30 40 46"/><path d="M16 28L22 38L28 28"/></svg>
    <b style="margin-top:8px">STAFF</b><small>Portal</small>
  </div>
  <div class="portal-item" style="top:408px">
    <svg width="46" height="50" viewBox="0 0 46 50" fill="none" stroke="#fff" stroke-width="2.2"><circle cx="14" cy="8" r="5"/><circle cx="32" cy="8" r="5"/><path d="M23 46C10 36 3 28 3 20C3 14 8 11 13 13C17 15 21 18 23 22C25 18 29 15 33 13C38 11 43 14 43 20C43 28 36 36 23 46Z"/></svg>
    <b style="margin-top:8px">PARENT</b><small>Portal</small>
  </div>
</section>

<section class="abs about">
  <h2>ABOUT US</h2>
  <h3>Lorem Ipsum is simply dummy text of the printing and typesetting industry.</h3>
  <p>Lorem Ipsum has been the industry's standard dummy text ever since the 1500s, when an unknown printer took a galley of type and scrambled it to make a type specimen book. It has survived not only five centuries, but also the leap into electronic typesetting, remaining essentially unchanged. It was popularised in the 1960s with the release of Letraset...</p>
  <span class="btn">Read More</span>
</section>

<svg class="abs" style="left:0;top:1055px" width="1200" height="100" viewBox="0 0 1200 100"><path fill="#f3f3f3" d="M0 20C200 100 450 115 700 55C900 5 1080 -5 1200 30V100H0Z"/></svg>
<div class="abs grey"></div>

<section>
  <svg class="abs photo" style="left:88px;top:1265px" width="456" height="259"><rect role="img" aria-label="Modern campus building with timber screens and flowering gardens" width="456" height="259" fill="#a7a493"/></svg>
  <div class="abs campus-box" style="left:398px;top:1322px"><h4>KESTREL VALE<br>CAMPUS</h4><span class="pill">&#9673; Live Location</span></div>
  <svg class="abs photo" style="left:622px;top:1265px" width="456" height="259"><defs><linearGradient id="sky" x1="0" y1="0" x2="0" y2="1"><stop offset="0" stop-color="#3b9ae0"/><stop offset=".6" stop-color="#a9c7d8"/><stop offset="1" stop-color="#4f7a3c"/></linearGradient></defs><rect role="img" aria-label="Campus grounds with a clock tower and sports oval" width="456" height="259" fill="url(#sky)"/></svg>
  <div class="abs campus-box" style="left:931px;top:1322px"><h4>MARLOW PARK<br>CAMPUS</h4><span class="pill pill-alt">&#9673; Live Location</span></div>
</section>

<svg class="abs" style="left:0;top:1590px" width="1200" height="180" viewBox="0 0 1200 180">
  <path fill="#2f7fc1" d="M0 110C200 40 500 20 750 70C950 110 1100 60 1200 20V180H0Z"/>
  <path fill="#083a66" d="M0 140C200 70 500 50 750 100C950 140 1100 95 1200 60V180H0Z"/>
</svg>
<div class="abs navy"></div>
<h2 class="abs ann-title">ANNOUNCEMENTS</h2>

<section>
  <svg class="abs" style="left:89px;top:1856px" width="316" height="217"><rect role="img" aria-label="Community open day poster" width="316" height="217" fill="#c9d3d6"/></svg>
  <div class="abs card-box" style="left:105px;top:2029px"><h5>Connecting with our community</h5><div class="meta"><span>&#9638; Nov 30, 2022</span><span>&#9719; 3:15 PM to 4:30 PM</span></div></div>
  <svg class="abs" style="left:442px;top:1856px" width="316" height="217"><rect role="img" aria-label="Collage of students at a science fair" width="316" height="217" fill="#4a7080"/></svg>
  <div class="abs card-box" style="left:459px;top:2029px"><h5>where curiosity inspires solution steam fest</h5><div class="meta"><span>&#9638; Oct 22, 2022</span><span>&#9719; 11 AM to 3 PM</span></div></div>
  <svg class="abs" style="left:795px;top:1856px" width="316" height="217"><rect role="img" aria-label="Two young students smiling in class" width="316" height="217" fill="#8a5a55"/></svg>
  <div class="abs card-box" style="left:812px;top:2029px"><h5>Connecting with our community</h5><div class="meta"><span>&#9638; Nov 30, 2022</span><span>&#9719; 3:15 PM to 4:30 PM</span></div></div>
  <div class="abs drag"><svg width="18" height="14" viewBox="0 0 18 14" fill="none" stroke="#222" stroke-width="1.6"><path d="M1 7H16M11 2L16 7L11 12"/></svg><br>DRAG</div>
</section>

<svg class="abs" style="left:0;top:2230px" width="1200" height="130" viewBox="0 0 1200 130">
  <path fill="#2f7fc1" d="M0 100C300 0 550 5 800 60C1000 105 1120 60 1200 0V0H0Z"/>
  <path fill="#083a66" d="M0 75C300 -20 550 -15 800 35C1000 75 1120 40 1200 -10V0H0Z"/>
  <path fill="#fff" d="M0 100C300 0 550 5 800 60C1000 105 1120 60 1200 0V130H0Z"/>
</svg>

<section>
  <div class="abs quick" style="left:170px;top:2427px">
    <svg width="46" height="44" viewBox="0 0 46 44" fill="none" stroke="#1a66a3" stroke-width="2"><rect x="2" y="4" width="40" height="34" rx="3"/><path d="M2 12H42M14 24H30M14 30H24"/></svg>
    <span>BOOK A<br>TOUR</span></div>
  <div class="abs quick" style="left:400px;top:2427px">
    <svg width="38" height="48" viewBox="0 0 38 48" fill="none" stroke="#1a66a3" stroke-width="2"><rect x="2" y="2" width="34" height="44" rx="3"/><path d="M2 10H36M9 20H29M9 27H29M9 34H22"/></svg>
    <span>ENROLMENT<br>APPLICATION<br>FORM</span></div>
  <div class="abs quick" style="left:631px;top:2427px">
    <svg width="48" height="50" viewBox="0 0 48 50" fill="none" stroke="#1a66a3" stroke-width="2"><circle cx="24" cy="14" r="9"/><path d="M4 28H44V46H4ZM24 28V46M4 12H8M40 12H44M24 0V3"/></svg>
    <span>PROSPECTUS</span></div>
  <div class="abs quick active" style="left:860px;top:2427px">
    <svg width="54" height="48" viewBox="0 0 54 48" fill="none" stroke="#fff" stroke-width="2"><circle cx="38" cy="14" r="12"/><path d="M35 11C35 7 42 7 42 11C42 14 38 14 38 17M38 20V21"/><path d="M4 20H26V38H14L6 44V38H4Z"/><path d="M9 27H21M9 32H18"/></svg>
    <span>FAQ</span></div>
</section>

<svg class="abs" style="left:0;top:2670px" width="1200" height="170" viewBox="0 0 1200 170">
  <path fill="#2f7fc1" d="M0 140C150 40 300 5 450 20C700 50 900 140 1100 90C1150 75 1180 50 1200 35V170H0Z"/>
  <path fill="#083a66" d="M0 165C150 65 300 30 450 45C700 75 900 165 1100 115C1150 100 1180 80 1200 65V170H0Z"/>
</svg>
<footer>
  <div class="abs foot"></div>
  <div class="abs ribbon"><h6>INFORMATION RIBBON</h6><p>Lorem Ipsum is simply dummy text of the printing and typesetting industry. Lorem Ipsum has been the industry's standard dummy text ever since the 1500s, when... <u>MORE</u></p></div>
  <div class="abs stat" style="left:726px;top:2896px;width:200px"><small>CRICOS PROVIDER NUMBER:</small><b>04812K</b></div>
  <div class="abs divider"></div>
  <div class="abs stat" style="left:973px;top:2896px;width:160px"><small>ABN:</small><b>52 184 733 609</b></div>
  <svg class="abs" style="left:1142px;top:2902px" width="20" height="24" viewBox="0 0 20 24"><path fill="#fff" d="M10 0L20 24L10 18L0 24Z"/></svg>
  <div class="abs bar">Bramwell College. All rights reserved. &nbsp;|&nbsp; Privacy, Disclaimer &amp; Copyright © 2023</div>
  <div class="abs social bottom-social" aria-label="Social links"><span></span><span></span><span></span></div>
</footer>

</body>
</html>
```